Yoga class opening. Little schedule for JUNE JULY and AUGUST

Flyer to promote an opening yoga class. The color of the docx haven't to be respected.

We want something joyfull, professional, clean and serious.

About the logo we oppened a contest at the same time so at the moment there is no logo but the logo color will be simple.

The phone number will change so you can poste a random one for the design that i can change by myself.

i recieved many creation in both side BUT i want something in 1 side :)

Yoga student. all age

It Professional

Yoga brook

Sans Serif

• The text present on the docx
• Some symbols about yoga ( Namasté signs, mandala, ... )
• Not too much details it has to be clear.

```html
<!DOCTYPE html>
<html lang="fr">
<head>
<meta charset="utf-8">
<title>Yoga Brook – Ouverture</title>
<link rel="stylesheet" href="https://fonts.googleapis.com/css2?family=Oswald:wght@400;500;700&family=Roboto+Condensed:wght@400;700&display=swap">
<style>
  :root{
    --page:#ebe6e1;
    --paper:#ffffff;
    --brown:#9b3d1c;
    --brown-dark:#7c2c12;
    --orange:#e8742a;
    --orange-soft:#ee9055;
    --peach:#f7c9a8;
    --peach-light:#fce5d4;
    --text-dark:#5a2a16;
  }
  *{box-sizing:border-box;margin:0;padding:0}
  html,body{width:1200px;height:831px;overflow:hidden;background:var(--page)}
  body{position:relative;font-family:"Roboto Condensed",Arial,sans-serif;color:var(--text-dark)}

  .flyer{position:absolute;left:320px;top:20px;width:560px;height:790px;background:var(--paper);overflow:hidden;box-shadow:0 2px 10px rgba(0,0,0,.12)}

  /* header */
  .brand-dot{position:absolute;left:20px;top:18px;width:62px;height:62px;border-radius:50%;background:var(--peach)}
  .brand-name{position:absolute;left:94px;top:6px;font-family:"Oswald",sans-serif;font-weight:500;font-size:56px;line-height:1;letter-spacing:1px;color:var(--brown)}
  .brand-tagline{position:absolute;left:96px;top:76px;font-family:"Oswald",sans-serif;font-size:12.5px;color:var(--orange);letter-spacing:.3px}

  /* ribbon + opening */
  .ribbon{position:absolute;left:0;top:104px;width:205px;height:42px;background:var(--brown);clip-path:polygon(0 0,100% 0,92% 50%,100% 100%,0 100%);display:flex;align-items:center;padding-left:26px;font-family:"Oswald",sans-serif;font-weight:700;font-size:24px;color:#fff;letter-spacing:.5px}
  .opening{position:absolute;right:22px;top:96px;text-align:right;font-family:"Oswald",sans-serif;font-weight:500;color:var(--brown);line-height:1.15}
  .opening .date{font-size:19px}
  .opening .address{font-size:14px}

  /* hero */
  .hero-block{position:absolute;left:0;top:162px;width:130px;height:70px;background:var(--brown)}
  .hero-photo{position:absolute;left:130px;top:162px;width:410px;height:150px;background:linear-gradient(180deg,#c35a6c 0%,#e58a5c 45%,#f7c27a 70%,#9a4a3c 100%)}

  /* left column */
  .schedule{position:absolute;left:14px;top:318px;width:292px;height:458px;background:var(--peach-light);padding-bottom:10px}
  .intro{background:var(--orange-soft);color:#fff;font-size:12px;line-height:1.25;padding:8px 12px}
  .month{margin:10px 12px 0}
  .month h2{font-family:"Oswald",sans-serif;font-weight:500;font-size:19px;color:var(--brown);line-height:1.1}
  .event{font-size:9.5px;font-weight:700;color:var(--brown);text-transform:uppercase;margin-top:3px;border-bottom:1px solid var(--peach);padding-bottom:2px}
  .slot{font-size:10.5px;color:var(--text-dark);line-height:1.5;border-bottom:1px solid #f3d2bb}

  /* right column */
  .om-medallion{position:absolute;left:338px;top:228px;width:196px;height:196px;border-radius:50%;background:radial-gradient(circle,var(--orange) 0 34%,#fbd9c1 35% 62%,var(--peach) 63% 100%)}
  .info{position:absolute;left:318px;top:440px;width:232px;text-align:center;font-family:"Oswald",sans-serif;color:var(--brown);line-height:1.15}
  .info .lead{font-size:16px;font-weight:400}
  .info .start{font-size:22px;font-weight:700;color:var(--orange)}
  .info .small{font-size:14px;margin-top:4px}
  .info .phone{font-size:30px;font-weight:700;color:var(--brown)}
  .info .page-name{font-size:17px;font-weight:500}
  .closing{position:absolute;left:300px;top:676px;width:260px;height:88px;background:var(--brown);clip-path:polygon(10% 0,100% 0,100% 100%,0 100%);display:flex;align-items:center;justify-content:center;text-align:center;font-family:"Oswald",sans-serif;font-weight:700;font-size:28px;line-height:1.05;color:#fff;padding-left:20px}
</style>
</head>
<body>
<main class="flyer">
  <span class="brand-dot"></span>
  <h1 class="brand-name">YOGA BROOK</h1>
  <p class="brand-tagline">NOUVEAU !! VOTRE STUDIO DE YOGA À LINDEVAL</p>

  <div class="ribbon">NOUVEAU !!</div>
  <div class="opening">
    <div class="date">OUVERTURE LE 6 JUIN 2016 AU</div>
    <div class="address">212 CHAUSSÉE DE VERLAINE</div>
    <div class="address">4270 LINDEVAL</div>
  </div>

  <div class="hero-block"></div>
  <div class="hero-photo" role="img" aria-label="Photo d'une personne méditant en posture du lotus face aux montagnes au coucher du soleil"></div>

  <section class="schedule">
    <p class="intro">En attendant le planning des cours de la rentrée, YOGA BROOK vous propose des stages et ateliers d'été.</p>

    <div class="month">
      <h2>JUIN</h2>
      <p class="event">Stage découverte du yoga 5 jours 80 €</p>
      <p class="slot">Du lundi 13 au vendredi 17 · 10h-12h ou 18h-20h</p>
      <p class="slot">Du lundi 20 au vendredi 24 · 10h-12h ou 18h-20h</p>
      <p class="event">Atelier gestion du stress 2 jours 30 €</p>
      <p class="slot">Samedi 25 juin · 10h-12h</p>
      <p class="slot">Dimanche 26 juin · 10h-12h</p>
    </div>

    <div class="month">
      <h2>JUILLET</h2>
      <p class="event">Stage initiation à l'ayurveda 5 jours 80 €</p>
      <p class="slot">Du lundi 4 au vendredi 8 · 10h-12h ou 18h-20h</p>
      <p class="slot">Du lundi 11 au vendredi 15 · 10h-12h ou 18h-20h</p>
      <p class="event">Atelier respiration et relaxation 2 jours 30 €</p>
      <p class="slot">Samedi 16 juillet · 10h-12h</p>
      <p class="slot">Dimanche 17 juillet · 10h-12h</p>
    </div>

    <div class="month">
      <h2>AOUT</h2>
      <p class="event">Stage découverte du yoga 5 jours 80 €</p>
      <p class="slot">Du lundi 8 au vendredi 12 · 10h-12h ou 18h-20h</p>
      <p class="slot">Du lundi 22 au vendredi 26 · 10h-12h ou 18h-20h</p>
    </div>
  </section>

  <div class="om-medallion" role="img" aria-label="Symbole Om entouré d'un mandala ornemental orange"></div>

  <div class="info">
    <p class="lead">Démarrage<br>du planning annuel le</p>
    <p class="start">5 septembre 2016</p>
    <p class="small">Plus d'info et inscription :</p>
    <p class="phone">600 123 456</p>
    <p class="small">Ou via notre page</p>
    <p class="page-name">Friendwall : yoga brook</p>
  </div>

  <div class="closing">UN BEL ETE<br>A TOUS !</div>
</main>
</body>
</html>
```